Beer labels for craft beer brewery

For a newly founded micro-brewery in Eastern Austria, we need beer labels to start production. We will be starting with three beer-variations, thus different 4 labels total (Basic label + 3 variations). The beers are made of natural ingredients (water, hop&malt) sourced locally and we are aiming to attain bio-certification. The motto is "Aus dem Tal ins Glas" (From the field to the bottle) and expresses the natural, circular and honest way of brewing beer. The Brewery's name is "Hofwaldbräu" (Hofwald-brewery), as in the history of the village, where the brewery is located, the former "head farmer" was nicknamend "Hofwald", as he talked like a politician and liked to inform his fellow citizens in the ways of the world...
Updates

Dear Designers, Customer has now uploaded their logo design for their business. Please use this and resubmit a label design using the Logo. Regards, QK Admin Leopold

Target Market(s)

regional Beer aficionados, local pub & restaurant patrons who value naturally manufactured premium craft beer.

Logo Text

Hofwaldbräu - aus dem Tal ins Glas (logo already designed)

Requirements
Must have
• Basic label and variations with color patterns and black&white version, end product: 4 recognizable individual beer labels as briefed.
Lable design & coloring must fit to brown color of beer bottles (no cans).
Nice to have
• Iconic label that is recognizeable and leaves a first impression...and "thirst" impression....
Should not have
• Beer can labels.

```html
<!DOCTYPE html>
<html lang="de">
<head>
<meta charset="utf-8">
<title>Hofwald – Etiketten</title>
<link rel="stylesheet" href="https://fonts.googleapis.com/css2?family=Oswald:wght@500;700&display=swap">
<style>
  :root{
    --bg:#5f5f5f;
    --white:#ffffff;
    --ink:#161616;
    --pale-base:#b5365c; --pale-a:#1a1446; --pale-b:#7ea2d8; --pale-badge:#f2b234;
    --juhu-base:#f2b234; --juhu-a:#e67d33; --juhu-b:#5b9bb0; --juhu-badge:#7ea2d8;
    --bilanz-base:#f8a060; --bilanz-a:#3c8a8a; --bilanz-b:#e8323e; --bilanz-badge:#f07070;
    --stille-base:#5ac8c4; --stille-a:#f06c6a; --stille-b:#1a5a5e; --stille-badge:#f08a58;
  }
  *{box-sizing:border-box;margin:0;padding:0}
  html,body{width:1200px;height:960px;overflow:hidden;background:var(--bg)}
  body{font-family:"Oswald",sans-serif;color:var(--white)}
  .range{position:relative;width:1200px;height:960px}
  .beer{position:absolute;top:236px;width:182px;margin-left:-91px}
  .beer:nth-child(1){left:240px}
  .beer:nth-child(2){left:480px}
  .beer:nth-child(3){left:722px}
  .beer:nth-child(4){left:962px}
  .neck-label{width:96px;height:72px;margin:0 auto;display:flex;flex-direction:column;align-items:center;justify-content:center;gap:6px;background:var(--base)}
  .neck-label .mark{width:34px;height:34px;border-radius:50%;background:var(--badge);border:4px solid var(--ink)}
  .neck-label .neck-name{font-size:10px;font-weight:700;letter-spacing:.8px;white-space:nowrap}
  .body-label{position:relative;margin-top:174px;width:182px;height:272px;overflow:hidden;background:var(--base)}
  .pattern{position:absolute;inset:0;background:
    radial-gradient(ellipse 55% 40% at 10% 75%,var(--b) 0 60%,transparent 62%),
    radial-gradient(ellipse 50% 45% at 90% 22%,var(--a) 0 60%,transparent 62%),
    linear-gradient(160deg,var(--base) 0 42%,var(--a) 42% 47%,var(--base) 47% 100%)}
  .content{position:relative;height:100%;display:flex;flex-direction:column;align-items:center;padding:6px 10px 8px}
  .top-line{font-size:5px;letter-spacing:.5px;white-space:nowrap}
  .brand{margin-top:12px;display:flex;flex-direction:column;align-items:center;gap:5px}
  .brand .mark{width:100px;height:100px;border-radius:50%;background:var(--badge);border:7px solid var(--ink)}
  .brand .brand-name{font-size:13px;font-weight:700;letter-spacing:3px}
  .beer-name{margin-top:auto;text-align:center;font-weight:700;line-height:1;text-transform:uppercase;white-space:nowrap}
  .beer-name .main{display:block;font-size:24px;letter-spacing:1px}
  .beer-name .sub{display:block;font-size:15px;letter-spacing:1px;margin-top:2px}
  .beer-name .big{font-size:34px}
  .origin{margin-top:6px;font-size:5px;letter-spacing:.5px;white-space:nowrap}
  .facts{width:100%;display:flex;justify-content:space-around;font-size:10px;font-weight:500;margin-top:4px;white-space:nowrap}
  .pale{--base:var(--pale-base);--a:var(--pale-a);--b:var(--pale-b);--badge:var(--pale-badge)}
  .juhu{--base:var(--juhu-base);--a:var(--juhu-a);--b:var(--juhu-b);--badge:var(--juhu-badge)}
  .bilanz{--base:var(--bilanz-base);--a:var(--bilanz-a);--b:var(--bilanz-b);--badge:var(--bilanz-badge)}
  .stille{--base:var(--stille-base);--a:var(--stille-a);--b:var(--stille-b);--badge:var(--stille-badge)}
</style>
</head>
<body>
<main class="range">
  <section class="beer pale">
    <div class="neck-label"><span class="mark"></span><span class="neck-name">PALE ALE</span></div>
    <div class="body-label">
      <div class="pattern" role="img" aria-label="Bunte fließende Wellenformen in Beere, Navy und Hellblau"></div>
      <div class="content">
        <p class="top-line">IPSUMLOREM IPSUMLOREM IPSUMLOREM</p>
        <div class="brand"><span class="mark"></span><span class="brand-name">HOFWALD</span></div>
        <h2 class="beer-name"><span class="main">Talboden</span><span class="sub">Pale Ale</span></h2>
        <p class="origin">BURGENLAND – MADE IN AUSTRIA</p>
        <p class="facts"><span>500ML</span><span>XX% ALC.VOL</span></p>
      </div>
    </div>
  </section>
  <section class="beer juhu">
    <div class="neck-label"><span class="mark"></span><span class="neck-name">JUHU</span></div>
    <div class="body-label">
      <div class="pattern" role="img" aria-label="Bunte fließende Wellenformen in Gelb, Orange und Blau"></div>
      <div class="content">
        <p class="top-line">IPSUMLOREM IPSUMLOREM IPSUMLOREM</p>
        <div class="brand"><span class="mark"></span><span class="brand-name">HOFWALD</span></div>
        <h2 class="beer-name"><span class="main big">Juhu</span></h2>
        <p class="origin">BURGENLAND – MADE IN AUSTRIA</p>
        <p class="facts"><span>500ML</span><span>XX% ALC.VOL</span></p>
      </div>
    </div>
  </section>
  <section class="beer bilanz">
    <div class="neck-label"><span class="mark"></span><span class="neck-name">BLANKE BILANZ</span></div>
    <div class="body-label">
      <div class="pattern" role="img" aria-label="Bunte fließende Wellenformen in Apricot, Petrol und Rot"></div>
      <div class="content">
        <p class="top-line">IPSUMLOREM IPSUMLOREM IPSUMLOREM</p>
        <div class="brand"><span class="mark"></span><span class="brand-name">HOFWALD</span></div>
        <h2 class="beer-name"><span class="main">Blanke</span><span class="main">Bilanz</span></h2>
        <p class="origin">BURGENLAND – MADE IN AUSTRIA</p>
        <p class="facts"><span>500ML</span><span>XX% ALC.VOL</span></p>
      </div>
    </div>
  </section>
  <section class="beer stille">
    <div class="neck-label"><span class="mark"></span><span class="neck-name">ABSPRACHEN</span></div>
    <div class="body-label">
      <div class="pattern" role="img" aria-label="Bunte fließende Wellenformen in Türkis, Koralle und Dunkelpetrol"></div>
      <div class="content">
        <p class="top-line">IPSUMLOREM IPSUMLOREM IPSUMLOREM</p>
        <div class="brand"><span class="mark"></span><span class="brand-name">HOFWALD</span></div>
        <h2 class="beer-name"><span class="main">Stille</span><span class="sub">Absprachen</span></h2>
        <p class="origin">BURGENLAND – MADE IN AUSTRIA</p>
        <p class="facts"><span>500ML</span><span>XX% ALC.VOL</span></p>
      </div>
    </div>
  </section>
</main>
</body>
</html>
```